Auto Detailing Facility Needs Facebook Cover Photo

Looking for a beautiful Facebook cover photo using our logo and a photo, including our business information. Does not have to use the photo provided but the logo must be in there. I want an eye-catching cover photo that promotes the luxury brand.

Website: www.glossbayauto.com
Phone: 508-555-0147
Address: 412 Lower Maple Rd Unit B-3 Franklin, MA 02091

Industry/Entity Type

Automotive

Colors

Designer to choose colors to be used in the design.

```html
<!DOCTYPE html>
<html lang="en">
<head>
<meta charset="utf-8">
<title>Gloss Bay Auto — Cover</title>
<link rel="stylesheet" href="https://fonts.googleapis.com/css2?family=Open+Sans:wght@400;700&display=swap">
<style>
  :root {
    --white: #ffffff;
    --ink: #2b2b2b;
    --green: #2e8b2a;
    --green-dark: #1f7a22;
    --green-light: #5cc259;
    --photo-top: #c9c6bf;
    --photo-mid: #e9b70e;
    --photo-low: #2a2a2a;
    --brand-red: #c8102e;
    --brand-black: #111111;
  }
  * { box-sizing: border-box; margin: 0; padding: 0; }
  html, body { width: 1200px; height: 456px; overflow: hidden; background: var(--white); }
  body { font-family: "Open Sans", Arial, sans-serif; color: var(--ink); }
  .cover { position: relative; width: 1200px; height: 456px; overflow: hidden; background: var(--white); }
  .backdrop { position: absolute; inset: 0; }
  .brand-name {
    position: absolute; right: 12px; top: 52px;
    display: flex; align-items: center; gap: 12px;
    font-size: 30px; font-weight: 400; letter-spacing: 3px; color: var(--ink);
  }
  .brand-name .mark { width: 18px; height: 18px; background: var(--ink); }
  .services { position: absolute; left: 790px; top: 122px; list-style: none; }
  .services li { display: flex; align-items: center; gap: 8px; font-size: 25px; height: 44px; }
  .services svg { width: 28px; height: 28px; }
  .website {
    position: absolute; right: 10px; top: 218px;
    display: flex; align-items: center; gap: 8px;
    font-size: 18px; color: var(--green);
  }
  .website svg { width: 26px; height: 26px; }
  .info-bar {
    position: absolute; left: 500px; top: 253px; width: 700px; height: 58px;
    background: var(--green);
    display: flex; align-items: center; gap: 18px; padding-left: 10px;
    color: var(--white); font-size: 18.5px;
  }
  .info-bar .item { display: flex; align-items: center; gap: 8px; }
  .info-bar svg { width: 30px; height: 30px; }
  .info-pointer { position: absolute; left: 508px; top: 310px; width: 40px; height: 22px; }
  .partners { position: absolute; left: 665px; top: 322px; width: 530px; height: 130px; }
  .partner { position: absolute; font-weight: 700; white-space: nowrap; }
  .p1 { left: 0; top: 4px; font-size: 34px; color: var(--brand-black); letter-spacing: 1px; }
  .p2 { left: 370px; top: 10px; font-size: 28px; color: var(--brand-black); }
  .p3 { left: 8px; top: 66px; font-size: 34px; color: var(--brand-black); }
  .p4 { left: 200px; top: 72px; font-size: 30px; color: var(--brand-red); }
  .p5 { left: 362px; top: 74px; font-size: 28px; color: var(--brand-red); }
</style>
</head>
<body>
<div class="cover">
  <svg class="backdrop" width="1200" height="456" viewBox="0 0 1200 456">
    <defs>
      <linearGradient id="photoTone" x1="0" y1="0" x2="0" y2="1">
        <stop offset="0" stop-color="var(--photo-top)"/>
        <stop offset="0.25" stop-color="var(--photo-mid)"/>
        <stop offset="0.7" stop-color="var(--photo-mid)"/>
        <stop offset="1" stop-color="var(--photo-low)"/>
      </linearGradient>
    </defs>
    <polygon role="img" aria-label="Photo of a yellow sports car parked in front of a garage" points="0,0 643,0 569,456 0,456" fill="url(#photoTone)"/>
    <polygon points="643,0 690,0 590,456 569,456" fill="var(--green-light)"/>
    <polygon points="690,0 833,0 590,456" fill="var(--green-dark)"/>
  </svg>

  <div class="brand-name"><span class="mark"></span>GLOSS BAY AUTO</div>

  <ul class="services">
    <li><svg viewBox="0 0 28 28"><rect x="2" y="6" width="18" height="18" fill="none" stroke="var(--green)" stroke-width="2.5"/><path d="M7 14 l5 6 L26 3" fill="none" stroke="var(--green)" stroke-width="4"/></svg>Automotive Detailing Service</li>
    <li><svg viewBox="0 0 28 28"><rect x="2" y="6" width="18" height="18" fill="none" stroke="var(--green)" stroke-width="2.5"/><path d="M7 14 l5 6 L26 3" fill="none" stroke="var(--green)" stroke-width="4"/></svg>Ceramic Coating</li>
  </ul>

  <div class="website">
    <svg viewBox="0 0 26 26" fill="none" stroke="var(--green)" stroke-width="1.8"><circle cx="13" cy="13" r="11"/><ellipse cx="13" cy="13" rx="5" ry="11"/><path d="M2 13h22M4 7h18M4 19h18"/></svg>
    www.glossbayauto.com
  </div>

  <div class="info-bar">
    <div class="item">
      <svg viewBox="0 0 30 30"><circle cx="15" cy="15" r="13" fill="none" stroke="var(--white)" stroke-width="2"/><path d="M10 8c-2 2 0 7 4 11s8 5 9 3l-3-3-2 1c-2-1-4-3-5-5l1-2z" fill="var(--white)"/></svg>
      508-555-0147
    </div>
    <div class="item">
      <svg viewBox="0 0 30 30"><path d="M15 3a8 8 0 0 0-8 8c0 6 8 14 8 14s8-8 8-14a8 8 0 0 0-8-8z" fill="none" stroke="var(--white)" stroke-width="2.5"/><circle cx="15" cy="11" r="3" fill="var(--white)"/><path d="M5 27h20" stroke="var(--white)" stroke-width="2"/></svg>
      412 Lower Maple Rd Unit B-3 Franklin, MA 02091
    </div>
  </div>
  <svg class="info-pointer" viewBox="0 0 40 22"><polygon points="0,0 40,0 20,22" fill="var(--green)"/></svg>

  <div class="partners">
    <span class="partner p1">LUMASHIELD</span>
    <span class="partner p2">VEXCOAT</span>
    <span class="partner p3">POLARIX</span>
    <span class="partner p4">BRIVANA</span>
    <span class="partner p5">Radenwell</span>
  </div>
</div>
</body>
</html>
```